Quorvex business card design

create modern and tech looking business card that is clean but effectively communciates that we are a cloud communications company.
Should have at minimum:
Employee Name
Postion
Phone Number
Email
website
create modern and tech looking business card that is clean but effectively communciates that we are a cloud communications company. We have two logo color schemes (attached) so would like to see designs both ways
Should have at minimum:
Employee Name
Postion
Phone Number
Email
website

```html
<!DOCTYPE html>
<html lang="en">
<head>
<meta charset="utf-8">
<title>Quorvex business card</title>
<link rel="stylesheet" href="https://fonts.googleapis.com/css2?family=Lato:wght@400;700&display=swap">
<style>
  :root {
    --backdrop: #2b2b2b;
    --card: #ffffff;
    --ink: #4a4a4a;
    --ink-strong: #333333;
    --purple: #5e3a8a;
    --cyan: #35b8d8;
    --rule: #6a6a6a;
  }
  * { box-sizing: border-box; margin: 0; padding: 0; }
  html, body { width: 1200px; height: 900px; overflow: hidden; }
  body {
    background: var(--backdrop);
    font-family: "Lato", sans-serif;
    position: relative;
  }
  .card {
    position: absolute;
    left: 250px;
    width: 700px;
    height: 400px;
    background: var(--card);
    box-shadow: 0 6px 18px rgba(0,0,0,0.45);
    overflow: hidden;
  }
  .card--front { top: 40px; }
  .card--back { top: 470px; }

  .brand-graphic {
    position: absolute;
    left: 0;
    top: 0;
    width: 62%;
    height: 100%;
    background: linear-gradient(120deg, var(--cyan) 0%, #4a7fc0 50%, var(--purple) 100%);
  }

  .brand {
    display: flex;
    align-items: center;
    gap: 12px;
    color: var(--ink);
    font-weight: 700;
    letter-spacing: 0.06em;
    text-transform: uppercase;
  }
  .brand__mark {
    background: var(--purple);
    flex: none;
  }
  .card--front .brand {
    position: absolute;
    right: 56px;
    top: 112px;
    font-size: 44px;
  }
  .card--front .brand__mark { width: 30px; height: 30px; }

  .card--back .brand {
    position: absolute;
    left: 60px;
    top: 180px;
    font-size: 34px;
  }
  .card--back .brand__mark { width: 24px; height: 24px; }

  .divider {
    position: absolute;
    left: 380px;
    top: 120px;
    width: 1px;
    height: 130px;
    background: var(--rule);
  }
  .contact {
    position: absolute;
    left: 410px;
    top: 118px;
    color: var(--ink);
  }
  .contact__name {
    font-size: 17px;
    font-weight: 700;
    color: var(--ink-strong);
  }
  .contact__role {
    font-size: 12px;
    letter-spacing: 0.04em;
    text-transform: uppercase;
    color: var(--purple);
    margin-bottom: 10px;
  }
  .contact__list { list-style: none; }
  .contact__item {
    display: flex;
    align-items: center;
    gap: 10px;
    font-size: 17px;
    line-height: 24px;
  }
  .contact__icon { width: 14px; height: 14px; flex: none; fill: var(--cyan); }
</style>
</head>
<body>
  <section class="card card--front" aria-label="Card front">
    <div class="brand-graphic" role="img" aria-label="Large cyan and purple brand graphic"></div>
    <div class="brand"><span class="brand__mark"></span>Quorvex</div>
  </section>

  <section class="card card--back" aria-label="Card back">
    <div class="brand"><span class="brand__mark"></span>Quorvex</div>
    <div class="divider"></div>
    <div class="contact">
      <p class="contact__name">Daniel Marlowe</p>
      <p class="contact__role">Managing Director</p>
      <ul class="contact__list">
        <li class="contact__item">
          <svg class="contact__icon" viewBox="0 0 16 16" aria-hidden="true"><path d="M3 9c0-3 2.2-5 5-5s5 2 5 5h-3V7.5H6V9z"/><rect x="4" y="9" width="8" height="4" rx="1"/></svg>
          5550 123 456
        </li>
        <li class="contact__item">
          <svg class="contact__icon" viewBox="0 0 16 16" aria-hidden="true"><path d="M1 3h14v1.5L8 9 1 4.5z"/><path d="M1 6l7 4.5L15 6v7H1z"/></svg>
          d.marlowe@quorvex.com
        </li>
        <li class="contact__item">
          <svg class="contact__icon" viewBox="0 0 16 16" aria-hidden="true"><circle cx="8" cy="8" r="6.5" fill="none" stroke="#35b8d8" stroke-width="1.4"/><ellipse cx="8" cy="8" rx="2.6" ry="6.5" fill="none" stroke="#35b8d8" stroke-width="1.2"/><path d="M1.5 8h13" stroke="#35b8d8" stroke-width="1.2"/></svg>
          www.quorvex.com
        </li>
      </ul>
    </div>
  </section>
</body>
</html>
```